Life Coach for Lawyers Business Card Design

Elegant, original, business card design for life coaching service for associate attorneys who work in big law and struggle with stress, overwhelm, and time management. Double sided design.

Target Market(s)

Women associate attorneys who work in big law and struggle with stress, overwhelm, and time management.

Industry/Entity Type

Life Coaching

Contact Information for Business Card

Marissa Pendrell
Life Coach
518.677.3941
calmbriefcounsel.net
marissa@calmbriefcounsel.net
@calmbriefcounsel (Instagram)

Font styles to use
Other font styles liked:
• Silver South font duo. See uploaded files.

Requirements
Must have
• Icons for phone, website, email, and Instagram instead of words. Specific colors used in my logo (171B2B, 421121, FFFFFF)
Nice to have
• Foil. Embossed. Feminine design.
Should not have
• Any colors other than those used in logo. See uploaded files.

```html
<!DOCTYPE html>
<html lang="en">
<head>
<meta charset="utf-8">
<title>Calm Brief Counsel – Business Cards</title>
<link href="https://fonts.googleapis.com/css2?family=Cormorant+Garamond:wght@500;600&family=Caveat:wght@500&display=swap" rel="stylesheet">
<style>
  :root {
    --navy: #171B2B;
    --plum: #421121;
    --white: #FFFFFF;
    --soft: rgba(255,255,255,0.85);
  }
  * { margin: 0; padding: 0; box-sizing: border-box; }
  html, body { width: 1200px; height: 1036px; overflow: hidden; }
  body {
    background: var(--navy);
    position: relative;
    font-family: "Cormorant Garamond", serif;
    color: var(--white);
  }
  .card {
    position: absolute;
    left: 270px;
    width: 660px;
    height: 377px;
    background: var(--plum);
    border-radius: 34px;
    box-shadow: 0 18px 40px rgba(0,0,0,0.45);
  }
  .card--front { top: 96px; }
  .card--back { top: 563px; }

  .front-mark {
    position: absolute;
    left: 50%; top: 50%;
    transform: translate(-50%, -50%);
    display: flex; align-items: center; gap: 16px;
  }
  .front-mark__circle {
    width: 30px; height: 30px;
    border: 2px solid var(--white);
    border-radius: 50%;
  }
  .front-mark__name {
    font-size: 34px; font-weight: 600;
    letter-spacing: 3px; text-transform: uppercase;
    color: var(--white);
  }

  .back-brand {
    position: absolute;
    left: 70px; top: 190px;
    font-size: 30px; font-weight: 600;
    letter-spacing: 2px; text-transform: uppercase;
    line-height: 1.05;
    color: var(--white);
  }
  .contact {
    position: absolute;
    left: 360px; top: 70px;
    width: 260px;
    text-align: center;
  }
  .contact__name {
    font-family: "Caveat", cursive;
    font-size: 38px; font-weight: 500;
    letter-spacing: 2px; text-transform: uppercase;
    line-height: 1;
  }
  .contact__rule { height: 1px; background: var(--soft); margin: 4px 10px 2px 40px; }
  .contact__role {
    font-size: 14px; font-weight: 600; letter-spacing: 2px;
    text-transform: uppercase;
  }
  .contact__rule--lower { margin: 2px 40px 10px 10px; }
  .contact__icons { display: flex; justify-content: center; gap: 8px; margin-bottom: 8px; }
  .contact__icons svg { width: 20px; height: 20px; }
  .contact__lines {
    list-style: none;
    font-size: 15px; font-weight: 600;
    letter-spacing: 0.5px; text-transform: uppercase;
    line-height: 1.35;
  }
  .contact__lines .gap { margin-top: 8px; }
</style>
</head>
<body>
  <section class="card card--front" aria-label="Card front">
    <div class="front-mark">
      <span class="front-mark__circle"></span>
      <span class="front-mark__name">Calm Brief Counsel</span>
    </div>
  </section>

  <section class="card card--back" aria-label="Card back">
    <div class="back-brand">Calm Brief<br>Counsel</div>
    <div class="contact">
      <div class="contact__name">Marissa Pendrell</div>
      <div class="contact__rule"></div>
      <div class="contact__role">Life Coach</div>
      <div class="contact__rule contact__rule--lower"></div>
      <div class="contact__icons">
        <svg viewBox="0 0 20 20" aria-label="phone"><circle cx="10" cy="10" r="9" fill="none" stroke="#fff" stroke-width="1.2"/><path d="M7 5.5l1.6 2-1 1.2a6 6 0 0 0 3.7 3.7l1.2-1 2 1.6-1 1.5C10 14.5 5.5 10 5.5 6.5z" fill="#fff"/></svg>
        <svg viewBox="0 0 20 20" aria-label="email"><circle cx="10" cy="10" r="9" fill="none" stroke="#fff" stroke-width="1.2"/><rect x="5.5" y="7" width="9" height="6.5" fill="none" stroke="#fff" stroke-width="1.1"/><path d="M5.5 7l4.5 3.6L14.5 7" fill="none" stroke="#fff" stroke-width="1.1"/></svg>
        <svg viewBox="0 0 20 20" aria-label="website"><circle cx="10" cy="10" r="9" fill="none" stroke="#fff" stroke-width="1.2"/><circle cx="10" cy="10" r="4.8" fill="none" stroke="#fff" stroke-width="1"/><ellipse cx="10" cy="10" rx="2" ry="4.8" fill="none" stroke="#fff" stroke-width="1"/><path d="M5.2 10h9.6" stroke="#fff" stroke-width="1"/></svg>
        <svg viewBox="0 0 20 20" aria-label="social"><circle cx="10" cy="10" r="9" fill="none" stroke="#fff" stroke-width="1.2"/><circle cx="10" cy="10" r="3.5" fill="#fff"/></svg>
      </div>
      <ul class="contact__lines">
        <li>518.677.3941</li>
        <li>calmbriefcounsel.net</li>
        <li class="gap">marissa@calmbriefcounsel.net</li>
        <li>calmbriefcounsel.net</li>
        <li>@calmbriefcounsel</li>
      </ul>
    </div>
  </section>
</body>
</html>
```